Global investment holding company - Business Card Design

Brenvik Holdings is a recently incorporated investment holding company. Based in Singapore, it has operations in global emerging markets in the transport & logistics, energy and livestock industries.

Its tagline "Growing Together Worldwide" reflects the company's philosophy of helping countries progress through partnerships which generate employment and share benefits with its society.

We are looking for a business card that reflects our global presence - incorporating the logo design into the business card design. It must have a sophisticated, modern & corporate feel.

Target Market(s)

Investors and high level governmental officials

Industry/Entity Type

Investment

Requirements
Must have
• - Use of shades of blue in logo

-Profile picture

- Name: Dennis Okoro
- Title: Chairman
- Email: dennis@brenvikholdings.example
- Mob: +65 9154 6081
- Tel: +65 6419 5820
- DID: + 65 6419 5821
- Address: 47 Marlow Road, #05-03, Singapore 048812

- website: www.brenvikholdings.example

```html
<!DOCTYPE html>
<html lang="en">
<head>
<meta charset="utf-8">
<title>Brenvik Holdings – Business Card</title>
<link rel="stylesheet" href="https://fonts.googleapis.com/css2?family=Open+Sans:wght@400;600&family=Questrial&display=swap">
<style>
  :root {
    --backdrop: #e6eaed;
    --card: #ffffff;
    --brand-blue: #1d4f95;
    --band-dark: #1f6cb4;
    --band-light: #6cc2f0;
    --text-dark: #3a3a3a;
    --text-grey: #6b6b6b;
    --link-blue: #2a5aa8;
    --photo-warm: #cdb796;
    --photo-navy: #2a3850;
  }
  * { box-sizing: border-box; margin: 0; padding: 0; }
  html, body {
    width: 1200px; height: 960px; overflow: hidden;
    background: var(--backdrop);
  }
  .canvas {
    position: relative; width: 1200px; height: 960px;
    display: flex; flex-direction: column; align-items: center;
    justify-content: center; gap: 40px;
  }
  .card {
    position: relative; width: 700px; height: 400px;
    background: var(--card);
    box-shadow: 0 6px 20px rgba(30, 50, 70, 0.18);
    overflow: hidden;
  }

  /* Front */
  .card-front {
    display: flex; flex-direction: column; align-items: center; justify-content: center;
  }
  .brand {
    display: flex; align-items: center; gap: 20px;
  }
  .brand-dot {
    width: 58px; height: 58px; border-radius: 50%; flex: none;
    background: var(--brand-blue);
  }
  .brand-name {
    font-family: "Open Sans", sans-serif; font-weight: 600;
    font-size: 46px; color: var(--brand-blue); letter-spacing: 0.5px;
    white-space: nowrap;
  }
  .tagline {
    margin-top: 26px;
    font-family: "Open Sans", sans-serif; font-weight: 400;
    font-size: 21px; letter-spacing: 2px; color: var(--text-grey);
    text-transform: uppercase; white-space: nowrap;
  }

  /* Back */
  .card-back { padding: 40px 0 40px 40px; display: flex; gap: 36px; }
  .profile-photo {
    width: 255px; height: 320px; flex: none;
    background: linear-gradient(180deg, var(--photo-warm) 0%, #b9a382 55%, var(--photo-navy) 100%);
  }
  .details { flex: 1; min-width: 0; font-family: "Questrial", sans-serif; color: var(--text-dark); }
  .name-band {
    margin-top: 8px; padding: 6px 16px 6px 18px;
    background: linear-gradient(90deg, var(--band-dark) 0%, var(--band-light) 100%);
    color: #fff;
  }
  .person-name { font-size: 24px; letter-spacing: 1px; line-height: 1.1; }
  .person-title { font-size: 17px; letter-spacing: 1px; line-height: 1.1; }
  .contact-list {
    margin-top: 20px;
    display: grid; grid-template-columns: 70px 1fr; row-gap: 2px;
    font-size: 16px; line-height: 1.15; white-space: nowrap;
  }
  .contact-list dd::before { content: ": "; }
  .address { margin-top: 14px; font-size: 16px; line-height: 1.25; }
  .website { margin-top: 22px; font-size: 18px; color: var(--link-blue); letter-spacing: 0.5px; white-space: nowrap; }
</style>
</head>
<body>
<main class="canvas">
  <section class="card card-front" aria-label="Business card front">
    <div class="brand">
      <span class="brand-dot"></span>
      <span class="brand-name">Brenvik Holdings</span>
    </div>
    <p class="tagline">Growing Together Worldwide</p>
  </section>

  <section class="card card-back" aria-label="Business card back">
    <div class="profile-photo" role="img" aria-label="Portrait photo of Dennis Okoro, Chairman, in a dark suit"></div>
    <div class="details">
      <div class="name-band">
        <p class="person-name">Dennis Okoro</p>
        <p class="person-title">Chairman</p>
      </div>
      <dl class="contact-list">
        <dt>Email</dt><dd>dennis@brenvikholdings.example</dd>
        <dt>Mob</dt><dd>+65 9154 6081</dd>
        <dt>Tel</dt><dd>+65 6419 5820</dd>
        <dt>DID</dt><dd>+ 65 6419 5821</dd>
      </dl>
      <p class="address">47 Marlow Road, #05-03,<br>Singapore 048812</p>
      <p class="website">www.brenvikholdings.example</p>
    </div>
  </section>
</main>
</body>
</html>
```